Mediapreneur looking for Wordpress Design for 55 plus community

I own the domain brightyearsahead.net and I have another contest going on to design the logo. I'm looking to build a site for those 55 plus who are living an active lifestyle.
I want to base my site off of this site, except make it more friendly to the 55 and over community.
http://www.kovaplume.com/
In my menu, I'd like to have the following categories. About Listen Read Watch Forum Contact and the ability to add more categories in the future (possible to external sites).
Listen will be podcasts, read will be blog posts, and watch will be videos (webinars)
Updates
I uploaded some images I bought from Pixelmarten that could be used in the design. Possibly a collage.
Videos are actually going to be webinars in the future. For example, I see a real estate agent presenting a webinar about active communities, or a financial adviser giving financial advice to my community. I was trying to simplify it for my audience, some of whom may not know what a webinar is, but I'd like to go with Webinar instead of Watch. I like read and listen, though. I plan on monetizing the site via sponsorship in podcasts and a directory of active communities I'm building. I'm possibly going to ask for sponsorship for webinars and write e-books in the future. Could you display podcasts on the home page? Maybe put the most recent blog posts below the podcasts? Also, can you put a form asking them to join my newsletter somewhere in prominent position? My call to actions are to get them to subscribe to my mailing list and listen to podcasts.
Thanks.
I changed my mind on using Webinar in the menu. I asked my mom what a webinar was and she gave me a blank look. I like the idea of using Watch instead. The menu should be in this order About Listen Read Watch Forum. Please put contact details in the header menu above the menu. Call...make up a phone number. Email..contact@brightyearsahead.net. In case you missed one of my previous public updates, Listen = Podcast, Read = Blog, and Watch = Webinar/Video.
Thanks and sorry for the changes.
55 and over
Build

```html
<!DOCTYPE html>
<html lang="en">
<head>
<meta charset="utf-8">
<title>Bright Years Ahead</title>
<link rel="stylesheet" href="https://fonts.googleapis.com/css2?family=Open+Sans:wght@300;400;600;700;800&display=swap">
<style>
:root{
  --ink-dark:#1e2a32;
  --teal:#2eab8c;
  --teal-dark:#23927a;
  --blue:#2a5ea8;
  --orange:#f5a317;
  --page:#e4e4e4;
  --card:#ffffff;
  --text:#333b40;
  --muted:#666e73;
  --line:#d6d6d6;
  --social-a:#3b5998;
  --social-b:#2aa7e0;
  --social-c:#c4302b;
}
*{box-sizing:border-box;margin:0;padding:0}
html,body{width:1200px;height:3502px;overflow:hidden}
body{font-family:"Open Sans",Arial,sans-serif;color:var(--text);background:var(--page);position:relative}
a{color:inherit;text-decoration:none}

/* header */
.site-header{position:absolute;top:0;left:0;width:1200px;height:65px;background:var(--ink-dark);display:flex;align-items:center}
.brand{position:absolute;left:98px;top:12px;font-size:32px;font-weight:300;color:#fff;letter-spacing:-.5px;line-height:40px}
.main-nav{position:absolute;left:398px;top:0;height:65px;display:flex;align-items:center;gap:0}
.main-nav a{font-size:12px;font-weight:700;color:#fff;text-transform:uppercase;margin-right:46px}
.login-btn{position:absolute;left:1025px;top:20px;width:76px;height:30px;background:var(--teal);color:#fff;font-size:11px;font-weight:700;display:flex;align-items:center;justify-content:center;border-radius:2px}

/* hero */
.hero{position:absolute;top:65px;left:0;width:1200px;height:477px;background:linear-gradient(100deg,#5f7d48 0%,#b98d7a 22%,#d9c3b2 40%,#8fa663 60%,#6f9142 80%,#a9c37c 100%)}
.hero-copy{position:absolute;left:738px;top:138px;color:#fff}
.hero-title{font-size:46px;font-weight:800;line-height:54px;letter-spacing:-.5px}
.hero-title .accent{color:var(--orange)}
.hero-sub{font-size:29px;font-weight:400;line-height:38px;text-transform:uppercase;margin-top:4px}
.join-btn{display:inline-flex;align-items:center;justify-content:center;margin-top:20px;width:175px;height:50px;background:var(--teal);color:#fff;font-weight:700;font-size:15px;border-radius:2px}

/* features band */
.feature-band{position:absolute;top:542px;left:0;width:1200px;height:331px;background:var(--ink-dark)}
.feature{position:absolute;top:48px;width:240px;text-align:center}
.feature-photo{width:180px;height:180px;margin:0 auto;border-radius:50%;border:5px solid #e8e8e8;box-shadow:0 14px 24px rgba(0,0,0,.55)}
.feature-label{display:block;margin-top:42px;font-size:13px;color:var(--teal)}

/* main */
.content{position:absolute;top:873px;left:0;width:1200px;height:2407px}
.section-title{position:absolute;left:98px;top:38px;font-size:26px;font-weight:700;color:var(--blue);text-transform:uppercase;letter-spacing:-.3px}
.posts{position:absolute;left:98px;top:96px;width:687px}
.post{background:var(--card);height:350px;margin-bottom:19px}
.post-meta{display:flex;height:82px;background:var(--teal);color:#fff;align-items:center}
.author-photo{width:93px;height:82px;background:linear-gradient(135deg,#b7a596,#e6ddd3 60%,#8c7f72)}
.author{width:200px;padding-left:28px}
.author-name{font-size:15px;font-weight:700;text-transform:uppercase;display:block}
.author-role{font-size:12px}
.post-date{display:flex;align-items:center;width:200px}
.post-date svg{margin-right:16px}
.post-date small{display:block;font-size:13px}
.post-date strong{font-size:14px;font-weight:700}
.post-actions{display:flex;gap:27px;margin-left:20px}
.post-body{display:flex;padding:26px 28px 0 28px}
.post-photo{flex:none;width:280px;height:210px}
.post-text{padding-left:38px}
.post-title{font-size:22px;font-weight:400;line-height:30px;color:var(--text);margin-top:4px}
.post-excerpt{font-size:12px;line-height:24px;color:var(--muted);margin-top:14px}

.pagination{position:absolute;right:415px;top:2318px;display:flex;gap:7px}
.pagination a{min-width:24px;height:26px;padding:0 8px;background:#fff;border:1px solid var(--line);font-size:11px;font-weight:600;display:flex;align-items:center;justify-content:center}
.pagination .wide{padding:0 14px}

/* sidebar */
.sidebar{position:absolute;left:812px;top:38px;width:290px}
.widget{background:var(--card);position:absolute;left:0;width:290px}
.widget-title{height:37px;background:var(--blue);color:#fff;font-size:13px;font-weight:700;text-transform:uppercase;padding-left:20px;display:flex;align-items:center}
.widget-body{padding:16px 20px}
.field-label{font-size:11px;color:var(--muted)}
.search-input{margin-top:12px;height:36px;border:1px solid var(--line);font-size:11px;color:var(--muted);padding:0 12px;display:flex;align-items:center}
.teal-btn{height:38px;margin-top:12px;background:var(--teal);color:#fff;font-size:12px;font-weight:700;text-transform:uppercase;display:flex;align-items:center;justify-content:center;gap:8px;border-radius:2px}
.widget-photo{height:180px;margin-bottom:14px}
.widget-text{font-size:11px;line-height:22px;color:var(--muted)}
.guests{color:var(--orange);font-weight:700}
.event-title{font-size:12px;font-weight:700;line-height:22px;text-transform:uppercase;color:var(--text)}
.event-video{height:180px;margin-top:14px;position:relative;background:linear-gradient(135deg,#4c6b30,#7f9b4f 45%,#3f5b2a)}
.event-video .play{position:absolute;left:50%;top:50%;width:54px;height:54px;margin:-27px 0 0 -27px;border-radius:50%;background:rgba(20,25,30,.75);display:flex;align-items:center;justify-content:center}
.promo{position:absolute;left:0;width:290px;height:133px;background:linear-gradient(120deg,#a9c6e4,#eef3f8 45%,#c5d7e8);display:flex;align-items:center;justify-content:flex-end;padding-right:18px}
.promo-text{font-size:20px;font-weight:800;line-height:22px;color:var(--teal);text-transform:uppercase;text-align:center}
.news-item{border:1px solid var(--line);padding:12px 16px;font-size:11px;line-height:22px;color:var(--muted);margin-bottom:10px;height:92px}
.news-item b{color:var(--text);font-weight:600}
.social{position:absolute;left:0;width:290px;height:85px;color:#fff;display:flex;align-items:center}
.social-mark{width:34px;height:34px;margin-left:24px;border-radius:3px;background:rgba(255,255,255,.9)}
.social-copy{margin-left:22px}
.social-copy small{display:block;font-size:12px}
.social-copy strong{font-size:26px;font-weight:400;line-height:28px}
.social-cta{position:absolute;right:0;top:0;width:26px;height:85px;background:rgba(0,0,0,.28);font-size:9px;font-weight:700;writing-mode:vertical-rl;display:flex;align-items:center;justify-content:center;text-transform:uppercase}
.popular-item{border:1px solid var(--line);padding:14px 16px;margin-bottom:12px;height:68px}
.popular-item b{display:block;font-size:11px;font-weight:600;color:var(--text)}
.popular-item span{font-size:10px;color:var(--teal)}

/* footer */
.site-footer{position:absolute;top:3280px;left:0;width:1200px;height:222px;background:var(--ink-dark);color:#fff;text-align:center}
.footer-brand{display:block;margin-top:50px;font-size:38px;font-weight:300;letter-spacing:-.5px}
.footer-nav{margin-top:26px;font-size:12px;display:flex;justify-content:center;gap:30px}
.footer-nav span{opacity:.8}
.copyright{margin-top:18px;font-size:12px;opacity:.85}
</style>
</head>
<body>

<svg width="0" height="0" style="position:absolute" aria-hidden="true">
  <defs>
    <symbol id="i-calendar" viewBox="0 0 36 36"><rect x="3" y="6" width="30" height="27" rx="2" fill="none" stroke="#fff" stroke-width="2"/><line x1="3" y1="13" x2="33" y2="13" stroke="#fff" stroke-width="2"/><line x1="10" y1="2" x2="10" y2="9" stroke="#fff" stroke-width="2"/><line x1="26" y1="2" x2="26" y2="9" stroke="#fff" stroke-width="2"/><g fill="#fff"><rect x="8" y="17" width="4" height="3"/><rect x="16" y="17" width="4" height="3"/><rect x="24" y="17" width="4" height="3"/><rect x="8" y="24" width="4" height="3"/><rect x="16" y="24" width="4" height="3"/><rect x="24" y="24" width="4" height="3"/></g></symbol>
    <symbol id="i-share" viewBox="0 0 32 32"><g fill="none" stroke="#fff" stroke-width="2"><circle cx="24" cy="7" r="4"/><circle cx="7" cy="16" r="4"/><circle cx="24" cy="25" r="4"/><line x1="11" y1="14" x2="20" y2="9"/><line x1="11" y1="18" x2="20" y2="23"/></g></symbol>
    <symbol id="i-download" viewBox="0 0 32 32"><g fill="none" stroke="#fff" stroke-width="2.2"><line x1="16" y1="3" x2="16" y2="20"/><polyline points="9,13 16,20 23,13"/><polyline points="4,21 4,28 28,28 28,21"/></g></symbol>
    <symbol id="i-play" viewBox="0 0 32 32"><circle cx="16" cy="16" r="13" fill="none" stroke="#fff" stroke-width="2.2"/><polygon points="13,10 22,16 13,22" fill="#fff"/></symbol>
  </defs>
</svg>

<header class="site-header">
  <a class="brand" href="#">brightyearsahead</a>
  <nav class="main-nav">
    <a href="#">Home</a><a href="#">About</a><a href="#">Listen</a><a href="#">Read</a><a href="#">Watch</a><a href="#">Forum</a><a href="#">Contact</a>
  </nav>
  <a class="login-btn" href="#">LOGIN</a>
</header>

<section class="hero" role="img" aria-label="Smiling older couple in hats embracing outdoors in a sunny green park">
  <div class="hero-copy">
    <h1 class="hero-title">BRIGHT YEARS <span class="accent">AHEAD</span></h1>
    <p class="hero-sub">55 plus who are living an<br>active lifestyle</p>
    <a class="join-btn" href="#">JOIN US NOW!</a>
  </div>
</section>

<section class="feature-band">
  <div class="feature" style="left:128px"><div class="feature-photo" role="img" aria-label="Three generations of a family smiling together" style="background:linear-gradient(135deg,#7fa3c9,#d9c7b4 55%,#8a9fb5)"></div><span class="feature-label">Subscribe &amp; Listen Today!</span></div>
  <div class="feature" style="left:361px"><div class="feature-photo" role="img" aria-label="Group of seniors exercising on a lawn" style="background:linear-gradient(135deg,#8db27a,#d8c9a8 55%,#6e9460)"></div><span class="feature-label">Free Training</span></div>
  <div class="feature" style="left:599px"><div class="feature-photo" role="img" aria-label="Older couple relaxing together on a couch" style="background:linear-gradient(135deg,#b9a999,#e8e0d6 55%,#9c8b7c)"></div><span class="feature-label">Amazing Story</span></div>
  <div class="feature" style="left:833px"><div class="feature-photo" role="img" aria-label="Older couple laughing together in a garden" style="background:linear-gradient(135deg,#5a7a3f,#b9866f 50%,#c04a7a)"></div><span class="feature-label">Our Community</span></div>
</section>

<main class="content">
  <h2 class="section-title">Featured Posts</h2>

  <div class="posts">
    <article class="post">
      <div class="post-meta">
        <div class="author-photo" role="img" aria-label="Author portrait"></div>
        <div class="author"><span class="author-name">Warren Mallory</span><span class="author-role">Business man</span></div>
        <div class="post-date"><svg width="36" height="36"><use href="#i-calendar"/></svg><div><small>Posted on</small><strong>27 March 2016</strong></div></div>
        <div class="post-actions"><svg width="32" height="32"><use href="#i-share"/></svg><svg width="32" height="32"><use href="#i-download"/></svg><svg width="32" height="32"><use href="#i-play"/></svg></div>
      </div>
      <div class="post-body">
        <div class="post-photo" role="img" aria-label="Older couple in winter jackets and scarves smiling in the snow" style="background:linear-gradient(135deg,#c7373b,#e9eef4 50%,#3c6ab0)"></div>
        <div class="post-text">
          <h3 class="post-title">Lorem Ipsum is simply dummy text of the printing</h3>
          <p class="post-excerpt">Lorem Ipsum is simply dummy text of the printing and typesetting industry. Lorem Ipsum has been the industry's standard dummy text ever since the 1500s, when an unknown printer took a galley of type and scrambled it to make a type specimen book. It has survived not only five centuries, but also the leap...</p>
        </div>
      </div>
    </article>

    <article class="post">
      <div class="post-meta">
        <div class="author-photo" role="img" aria-label="Author portrait" style="background:linear-gradient(135deg,#c9a37d,#efe3d2 60%,#9a7c61)"></div>
        <div class="author"><span class="author-name">Warren Mallory</span><span class="author-role">Business man</span></div>
        <div class="post-date"><svg width="36" height="36"><use href="#i-calendar"/></svg><div><small>Posted on</small><strong>27 March 2016</strong></div></div>
        <div class="post-actions"><svg width="32" height="32"><use href="#i-share"/></svg><svg width="32" height="32"><use href="#i-download"/></svg><svg width="32" height="32"><use href="#i-play"/></svg></div>
      </div>
      <div class="post-body">
        <div class="post-photo" role="img" aria-label="Older couple giving a thumbs up indoors" style="background:linear-gradient(135deg,#d9d2c8,#f1ece6 50%,#b9ab9b)"></div>
        <div class="post-text">
          <h3 class="post-title">Lorem Ipsum is simply dummy text of the printing</h3>
          <p class="post-excerpt">Lorem Ipsum is simply dummy text of the printing and typesetting industry. Lorem Ipsum has been the industry's standard dummy text ever since the 1500s, when an unknown printer took a galley of type and scrambled it to make a type specimen book. It has survived not only five centuries, but also the leap...</p>
        </div>
      </div>
    </article>

    <article class="post">
      <div class="post-meta">
        <div class="author-photo" role="img" aria-label="Author portrait"></div>
        <div class="author"><span class="author-name">Warren Mallory</span><span class="author-role">Business man</span></div>
        <div class="post-date"><svg width="36" height="36"><use href="#i-calendar"/></svg><div><small>Posted on</small><strong>27 March 2016</strong></div></div>
        <div class="post-actions"><svg width="32" height="32"><use href="#i-share"/></svg><svg width="32" height="32"><use href="#i-download"/></svg><svg width="32" height="32"><use href="#i-play"/></svg></div>
      </div>
      <div class="post-body">
        <div class="post-photo" role="img" aria-label="Older couple walking in an autumn park" style="background:linear-gradient(135deg,#c77a2a,#8aa0c8 50%,#5b6e32)"></div>
        <div class="post-text">
          <h3 class="post-title">Lorem Ipsum is simply dummy text of the printing</h3>
          <p class="post-excerpt">Lorem Ipsum is simply dummy text of the printing and typesetting industry. Lorem Ipsum has been the industry's standard dummy text ever since the 1500s, when an unknown printer took a galley of type and scrambled it to make a type specimen book. It has survived not only five centuries, but also the leap...</p>
        </div>
      </div>
    </article>

    <article class="post">
      <div class="post-meta">
        <div class="author-photo" role="img" aria-label="Author portrait" style="background:linear-gradient(135deg,#8a6a4e,#e9e2d6 60%,#6e5440)"></div>
        <div class="author"><span class="author-name">Warren Mallory</span><span class="author-role">Business man</span></div>
        <div class="post-date"><svg width="36" height="36"><use href="#i-calendar"/></svg><div><small>Posted on</small><strong>27 March 2016</strong></div></div>
        <div class="post-actions"><svg width="32" height="32"><use href="#i-share"/></svg><svg width="32" height="32"><use href="#i-download"/></svg><svg width="32" height="32"><use href="#i-play"/></svg></div>
      </div>
      <div class="post-body">
        <div class="post-photo" role="img" aria-label="Smiling older couple in light blue shirts" style="background:linear-gradient(135deg,#a9c3de,#f2ede6 50%,#7fa0c6)"></div>
        <div class="post-text">
          <h3 class="post-title">Lorem Ipsum is simply dummy text of the printing</h3>
          <p class="post-excerpt">Lorem Ipsum is simply dummy text of the printing and typesetting industry. Lorem Ipsum has been the industry's standard dummy text ever since the 1500s, when an unknown printer took a galley of type and scrambled it to make a type specimen book. It has survived not only five centuries, but also the leap...</p>
        </div>
      </div>
    </article>

    <article class="post">
      <div class="post-meta">
        <div class="author-photo" role="img" aria-label="Author portrait" style="background:linear-gradient(135deg,#c2475e,#6e4a3a 60%,#b98a6a)"></div>
        <div class="author"><span class="author-name">Warren Mallory</span><span class="author-role">Business man</span></div>
        <div class="post-date"><svg width="36" height="36"><use href="#i-calendar"/></svg><div><small>Posted on</small><strong>27 March 2016</strong></div></div>
        <div class="post-actions"><svg width="32" height="32"><use href="#i-share"/></svg><svg width="32" height="32"><use href="#i-download"/></svg><svg width="32" height="32"><use href="#i-play"/></svg></div>
      </div>
      <div class="post-body">
        <div class="post-photo" role="img" aria-label="Two older women power walking with water bottles" style="background:linear-gradient(135deg,#7fb04e,#d6e6a9 50%,#5d8e3a)"></div>
        <div class="post-text">
          <h3 class="post-title">Lorem Ipsum is simply dummy text of the printing</h3>
          <p class="post-excerpt">Lorem Ipsum is simply dummy text of the printing and typesetting industry. Lorem Ipsum has been the industry's standard dummy text ever since the 1500s, when an unknown printer took a galley of type and scrambled it to make a type specimen book. It has survived not only five centuries, but also the leap...</p>
        </div>
      </div>
    </article>

    <article class="post">
      <div class="post-meta">
        <div class="author-photo" role="img" aria-label="Author portrait" style="background:linear-gradient(135deg,#d0a070,#f3e7d8 60%,#b4805a)"></div>
        <div class="author"><span class="author-name">Warren Mallory</span><span class="author-role">Business man</span></div>
        <div class="post-date"><svg width="36" height="36"><use href="#i-calendar"/></svg><div><small>Posted on</small><strong>27 March 2016</strong></div></div>
        <div class="post-actions"><svg width="32" height="32"><use href="#i-share"/></svg><svg width="32" height="32"><use href="#i-download"/></svg><svg width="32" height="32"><use href="#i-play"/></svg></div>
      </div>
      <div class="post-body">
        <div class="post-photo" role="img" aria-label="Older couple fishing together on a dock" style="background:linear-gradient(135deg,#4e6b3a,#d77f9a 50%,#7a8c5a)"></div>
        <div class="post-text">
          <h3 class="post-title">Lorem Ipsum is simply dummy text of the printing</h3>
          <p class="post-excerpt">Lorem Ipsum is simply dummy text of the printing and typesetting industry. Lorem Ipsum has been the industry's standard dummy text ever since the 1500s, when an unknown printer took a galley of type and scrambled it to make a type specimen book. It has survived not only five centuries, but also the leap...</p>
        </div>
      </div>
    </article>
  </div>

  <nav class="pagination">
    <a class="wide" href="#">Prev</a><a href="#">1</a><a href="#">2</a><a href="#">3</a><a href="#">4</a><a href="#">5</a><a href="#">6</a><a href="#">...</a><a href="#">22</a><a class="wide" href="#">Next</a>
  </nav>

  <aside class="sidebar">
    <section class="widget" style="top:0;height:175px">
      <h4 class="widget-title">Search</h4>
      <div class="widget-body">
        <p class="field-label">Search by keyword</p>
        <div class="search-input">Search...</div>
        <a class="teal-btn" href="#"><svg width="13" height="13" viewBox="0 0 14 14"><circle cx="6" cy="6" r="4.5" fill="none" stroke="#fff" stroke-width="2"/><line x1="9.5" y1="9.5" x2="13" y2="13" stroke="#fff" stroke-width="2"/></svg>Search Now</a>
      </div>
    </section>

    <section class="widget" style="top:205px;height:437px">
      <h4 class="widget-title">About Bright Years Ahead</h4>
      <div class="widget-body">
        <div class="widget-photo" role="img" aria-label="Older couple smiling together outdoors" style="background:linear-gradient(135deg,#8fb36a,#e7ddd0 50%,#6d9450)"></div>
        <p class="widget-text">Lorem Ipsum is simply dummy text of the printing and typesetting industry. Lorem Ipsum has been the industry's standard dummy text ever since the 1500s, when an unknown printer took a galley of type and scrambled...</p>
        <a class="teal-btn" href="#">Read More Info</a>
      </div>
    </section>

    <section class="widget" style="top:660px;height:89px">
      <h4 class="widget-title">Who's Online</h4>
      <div class="widget-body"><p class="widget-text">We have <span class="guests">5 guests</span> online</p></div>
    </section>

    <section class="widget" style="top:770px;height:292px">
      <h4 class="widget-title">Recent Event</h4>
      <div class="widget-body">
        <p class="event-title">Lorem Ipsum is simply dummy text of the printing</p>
        <div class="event-video" role="img" aria-label="Video still of an older couple cycling on a forest path">
          <span class="play"><svg width="20" height="20" viewBox="0 0 20 20"><polygon points="5,2 18,10 5,18" fill="#fff"/></svg></span>
        </div>
      </div>
    </section>

    <div class="promo" style="top:1097px" role="img" aria-label="Older couple in winter clothes sledding in the snow">
      <span class="promo-text">Living an<br>active lifestyle</span>
    </div>

    <section class="widget" style="top:1254px;height:345px">
      <h4 class="widget-title">The Latest News</h4>
      <div class="widget-body">
        <p class="news-item"><b>Lorem Ipsum is simply dummy text of the printing and typesetting industry. Lorem</b> Ipsum the industry's standard...</p>
        <p class="news-item"><b>Lorem Ipsum is simply dummy text of the printing and typesetting industry. Lorem</b> Ipsum the industry's standard...</p>
        <p class="news-item"><b>Lorem Ipsum is simply dummy text of the printing and typesetting industry. Lorem</b> Ipsum the industry's standard...</p>
      </div>
    </section>

    <a class="social" href="#" style="top:1639px;background:var(--social-a)"><span class="social-mark"></span><span class="social-copy"><small>Connect with</small><strong>Circlepage</strong></span><span class="social-cta">Click here</span></a>
    <a class="social" href="#" style="top:1742px;background:var(--social-b)"><span class="social-mark"></span><span class="social-copy"><small>Connect with</small><strong>Chirpline</strong></span><span class="social-cta">Click here</span></a>
    <a class="social" href="#" style="top:1844px;background:var(--social-c)"><span class="social-mark"></span><span class="social-copy"><small>Connect with</small><strong>Reelhouse</strong></span><span class="social-cta">Click here</span></a>

    <section class="widget" style="top:1949px;height:374px">
      <h4 class="widget-title">Popular Posts</h4>
      <div class="widget-body">
        <div class="popular-item"><b>Lorem Ipsum is simply dummy text</b><span>Posted on 27 March 2015</span></div>
        <div class="popular-item"><b>Lorem Ipsum is simply dummy text</b><span>Posted on 27 March 2015</span></div>
        <div class="popular-item"><b>Lorem Ipsum is simply dummy text</b><span>Posted on 27 March 2015</span></div>
        <div class="popular-item"><b>Lorem Ipsum is simply dummy text</b><span>Posted on 27 March 2015</span></div>
      </div>
    </section>
  </aside>
</main>

<footer class="site-footer">
  <a class="footer-brand" href="#">brightyearsahead</a>
  <nav class="footer-nav">
    <a href="#">Home</a><span>/</span><a href="#">About</a><span>/</span><a href="#">Listen</a><span>/</span><a href="#">Read</a><span>/</span><a href="#">Watch</a><span>/</span><a href="#">Forum</a><span>/</span><a href="#">Contact</a>
  </nav>
  <p class="copyright">© 2016, Bright Years Ahead. All rights reserved.</p>
</footer>

</body>
</html>
```